we need an experienced designer to design the tube for our toothpaste

Design guidelines:
1. On the front side, our product logo (‘Q2786’) should be prominent enough.
2. Our brand logo (‘quorlume’) could be small-size and it's just a trademark indeed.

Some information here for your reference:
1. The color of toothpaste cap is white.
2. We hope that the primary color in the design is blue.
3.‘F’ in ‘Q2786’ stands for ‘quorlume’ and ‘fluoride’.
4. We will use aluminum-plastic composite materials to make toothpaste tubes. In addition to the design, we also hope that you can make relevant suggestions on the special requirements of printing.

At last, we hope that you could submit both 2D design and 3D visual effects.

Attachments:

Colors
0094D4
00A9DD
6FCCEA
C7EBF8
E9F6FB

Requirements
Must have
• as attached

```html
<!DOCTYPE html>
<html lang="en">
<head>
<meta charset="utf-8">
<title>Q2786 Orthodontic Toothpaste – Tube Label</title>
<link rel="stylesheet" href="https://fonts.googleapis.com/css2?family=Poppins:wght@700;800&family=Saira+Condensed:wght@500;600&family=Roboto+Condensed:wght@300;400&display=swap">
<style>
  :root {
    --page: #ffffff;
    --ink-blue: #1c4fd8;
    --strip-blue: #1f57e2;
    --panel-deep: #1d5ae6;
    --panel-mid: #2f86ef;
    --panel-light: #6fccea;
    --white: #ffffff;
    --line: #111111;
    --cut: #e0322b;
    --gum: #e8559a;
    --gum-bg: #f7c6d6;
  }
  * { margin: 0; padding: 0; box-sizing: border-box; }
  html, body { width: 1200px; height: 780px; overflow: hidden; background: var(--page); }
  .canvas { position: relative; width: 1200px; height: 780px; }

  .spine-strip { position: absolute; left: 61px; top: 36px; width: 64px; height: 706px; background: var(--strip-blue); }
  .front-panel {
    position: absolute; left: 136px; top: 36px; width: 507px; height: 706px;
    background:
      radial-gradient(ellipse 420px 170px at 62% 14%, rgba(233,246,251,.9), rgba(199,235,248,.35) 55%, transparent 75%),
      linear-gradient(165deg, var(--panel-mid) 0%, var(--panel-deep) 45%, var(--panel-deep) 62%, #3f9ff2 88%, var(--panel-light) 100%);
  }

  .trim-outer { position: absolute; left: 70px; top: 45px; width: 1048px; height: 688px; border: 1px solid var(--line); }
  .trim-inner { position: absolute; left: 75px; top: 52px; width: 1035px; height: 667px; border: 1px solid var(--line); }
  .fold { position: absolute; left: 70px; width: 1048px; height: 0; border-top: 1px solid var(--line); }
  .cut-line { position: absolute; left: 70px; width: 1126px; height: 0; border-top: 1.2px dashed var(--cut); }

  .brand-name {
    position: absolute; left: 155px; top: 120px;
    font: 700 30px/1 "Poppins", sans-serif; color: var(--white); letter-spacing: .5px;
  }

  .product-mark {
    position: absolute; left: 152px; top: 188px;
    font: 800 110px/1 "Poppins", sans-serif; color: var(--white); letter-spacing: 2px;
  }

  .product-type {
    position: absolute; left: 155px; top: 296px;
    font: 800 27px/1 "Poppins", sans-serif; color: var(--white); letter-spacing: .3px;
  }
  .spec { position: absolute; top: 334px; font: 600 30px/1 "Saira Condensed", sans-serif; color: var(--white); }
  .spec-fluoride { left: 155px; }
  .spec-flavour { left: 426px; }

  .tagline {
    position: absolute; left: 157px; top: 446px;
    font: 600 28px/34px "Saira Condensed", sans-serif; color: var(--white); letter-spacing: .4px;
  }
  .illustration { position: absolute; top: 515px; width: 130px; height: 85px; }
  .illustration-plain { left: 161px; background: linear-gradient(180deg, var(--gum-bg) 0%, var(--white) 30%, var(--gum) 62%, var(--gum-bg) 100%); }
  .illustration-braces { left: 306px; background: linear-gradient(180deg, var(--gum-bg) 0%, #dfe6ee 32%, var(--gum) 62%, var(--gum-bg) 100%); }

  .benefits { position: absolute; left: 157px; top: 606px; list-style: none; }
  .benefits li { font: 600 21px/32px "Saira Condensed", sans-serif; color: var(--white); letter-spacing: .3px; }

  .claims {
    position: absolute; left: 665px; top: 192px;
    font: 600 25px/32.5px "Saira Condensed", sans-serif; color: var(--ink-blue); letter-spacing: .4px;
  }
  .net-weight { position: absolute; left: 665px; top: 338px; font: 600 25px/1 "Saira Condensed", sans-serif; color: var(--ink-blue); }

  .info { position: absolute; left: 667px; width: 422px; color: var(--ink-blue); font-family: "Roboto Condensed", sans-serif; font-weight: 300; }
  .info h3 { font-weight: 300; font-size: 16px; line-height: 20px; }
  .directions { top: 444px; }
  .directions p { font-size: 16.5px; line-height: 22px; }
  .ingredients { top: 547px; }
  .ingredients p { font-size: 14.6px; line-height: 19px; }
  .warnings { top: 654px; }
  .warnings p { font-size: 15px; line-height: 19px; }
</style>
</head>
<body>
<div class="canvas">
  <div class="spine-strip"></div>
  <div class="front-panel"></div>

  <div class="trim-outer"></div>
  <div class="trim-inner"></div>
  <div class="fold" style="top:87px"></div>
  <div class="fold" style="top:417px"></div>

  <div class="brand-name">quorlume</div>

  <div class="product-mark">Q2786</div>
  <div class="product-type">ORTHODONTIC TOOTHPASTE</div>
  <div class="spec spec-fluoride">Fluoride 1450 ppm</div>
  <div class="spec spec-flavour">Double Mint</div>

  <div class="tagline">PREMIUM ORAL CARE DURING<br>ORTHODONTIC TREATMENT</div>
  <div class="illustration illustration-plain" role="img" aria-label="Illustration of clean teeth and gums"></div>
  <div class="illustration illustration-braces" role="img" aria-label="Illustration of teeth with metal braces"></div>

  <ul class="benefits">
    <li>1 Prevent Cavity</li>
    <li>2 Freshen Breath</li>
    <li>3 Strengthen Teeth</li>
  </ul>

  <div class="claims">ENHANCED CAVITY PREVENTION<br>AND GUM PROTECTION<br>FOR USE WHEN WEARING METAL<br>BRACES AND CLEAR ALIGNERS</div>
  <div class="net-weight">NET WT. 85g</div>

  <section class="info directions">
    <h3>Directions</h3>
    <p>Apply at least one inch strip of the product onto a soft bristle toothbrush. Brush teeth thoroughly, for at least three minutes twice a day.</p>
  </section>
  <section class="info ingredients">
    <h3>Ingredients:</h3>
    <p>Aqua, Sorbitol, Hydrated Silica, Glycerin, PEG-12, Sodium Lauryl Sulfate, Aroma, Cellulose Gum, Titanium Dioxide, Potassium Sorbate, Allantoin, Sodium Fluoride, Citric Acid, Peppermint Essence, Sodium Saccharin, CI 47005, CI 42090, Cinnamal.</p>
  </section>
  <section class="info warnings">
    <h3>Warnings:</h3>
    <p>Do not ingest. Keep out of reach of children under 6 years of age.</p>
  </section>

  <div class="cut-line" style="top:252px"></div>
  <div class="cut-line" style="top:582px"></div>
</div>
</body>
</html>
```